Need Business Card for our Indian Grocery Store

Industry/Entity Type

Grocery Store

Contact Information for Business Card

Manoj Baweja
Director

Store Locations:

Thomastown
482 Elm Parade
P: 03 9172 5843

Reservoir
613 Carlow Road
P: 03 9238 6014

email: kvtmarts@mailnest.example

Requirements
Must have
• Our logo Colours

```html
<!DOCTYPE html>
<html lang="en">
<head>
<meta charset="utf-8">
<title>KVT Groceries &amp; Spices – Business Card</title>
<link href="https://fonts.googleapis.com/css2?family=Lato:wght@300;400;700&display=swap" rel="stylesheet">
<style>
  :root {
    --backdrop: #3b3c40;
    --charcoal: #2d2f33;
    --slate: #44494f;
    --steel: #5f6b73;
    --red: #e31e25;
    --red-light: #e94b51;
    --red-dark: #b71f26;
    --white: #ffffff;
    --muted: #c9cbce;
  }
  * { margin: 0; padding: 0; box-sizing: border-box; }
  html, body { width: 1200px; height: 1000px; overflow: hidden; }
  body {
    background: var(--backdrop);
    font-family: "Lato", Arial, sans-serif;
    color: var(--white);
    position: relative;
  }
  .card { position: absolute; left: 269px; width: 670px; height: 385px; overflow: hidden; }
  .card--front { top: 78px; background: var(--red); }
  .card--back { top: 534px; background: var(--white); }

  /* front: header band */
  .header-band { position: absolute; left: 0; top: 0; width: 670px; height: 140px; background: var(--charcoal); }
  .person { position: absolute; left: 57px; top: 46px; }
  .person__name { font-size: 34px; font-weight: 700; letter-spacing: -0.3px; line-height: 1; }
  .person__role { font-size: 20px; font-weight: 300; color: var(--muted); margin-top: 8px; }
  .header-divider { position: absolute; left: 335px; top: 37px; width: 1px; height: 90px; background: #7a7d82; }
  .store { position: absolute; left: 380px; top: 43px; width: 185px; text-align: center; font-size: 19px; font-weight: 300; line-height: 24.5px; color: var(--muted); }

  /* front: brand block */
  .brand { position: absolute; left: 40px; top: 180px; width: 262px; text-align: center; }
  .brand__name { font-size: 34px; font-weight: 700; line-height: 1.15; color: var(--white); }

  /* front: contact list */
  .contact { position: absolute; left: 336px; width: 334px; display: flex; }
  .contact__icon { width: 47px; height: 100%; display: flex; align-items: center; justify-content: center; }
  .contact__text { position: relative; flex: 1; padding-left: 30px; font-size: 19px; line-height: 21px; }
  .contact__text::before {
    content: ""; position: absolute; left: 0; top: 50%; margin-top: -6px;
    border-style: solid; border-width: 6px 0 6px 7px; border-color: transparent;
  }
  .contact--phone { top: 154px; height: 59px; }
  .contact--phone .contact__icon { background: var(--charcoal); }
  .contact--phone .contact__text { background: var(--red-light); padding-top: 15px; }
  .contact--phone .contact__text::before { border-left-color: var(--charcoal); }
  .contact--mail { top: 213px; height: 60px; }
  .contact--mail .contact__icon { background: var(--slate); }
  .contact--mail .contact__text { background: var(--red); padding-top: 18px; }
  .contact--mail .contact__text::before { border-left-color: var(--slate); }
  .contact--place { top: 273px; height: 112px; }
  .contact--place .contact__icon { background: var(--steel); align-items: flex-start; padding-top: 16px; }
  .contact--place .contact__text { background: var(--red-dark); padding-top: 13px; }
  .contact--place .contact__text::before { border-left-color: var(--steel); top: 30px; }

  /* back */
  .back-band { position: absolute; left: 0; width: 670px; background: var(--red); }
  .back-band--top { top: 0; height: 91px; }
  .back-band--bottom { top: 295px; height: 90px; display: flex; align-items: center; justify-content: center; gap: 16px; font-size: 23px; }
  .back-brand { position: absolute; left: 0; top: 91px; width: 670px; height: 204px; display: flex; flex-direction: column; align-items: center; justify-content: center; }
  .back-brand__name { font-size: 40px; font-weight: 700; color: var(--red); line-height: 1.1; }
  .back-brand__tagline { font-size: 15px; font-weight: 400; color: var(--red); margin-top: 12px; }
</style>
</head>
<body>

<section class="card card--front">
  <div class="header-band">
    <div class="person">
      <div class="person__name">Manoj Baweja</div>
      <div class="person__role">Director</div>
    </div>
    <div class="header-divider"></div>
    <div class="store">Reservoir<br>613 Carlow Road<br>03 9238 6014</div>
  </div>

  <div class="brand">
    <div class="brand__name">KVT Groceries &amp; Spices</div>
  </div>

  <div class="contact contact--phone">
    <div class="contact__icon">
      <svg width="22" height="22" viewBox="0 0 24 24" fill="#fff"><path d="M6.6 10.8a15.1 15.1 0 0 0 6.6 6.6l2.2-2.2c.3-.3.7-.4 1-.2 1.1.4 2.3.6 3.6.6.6 0 1 .4 1 1V20c0 .6-.4 1-1 1A17 17 0 0 1 3 4c0-.6.4-1 1-1h3.5c.6 0 1 .4 1 1 0 1.3.2 2.5.6 3.6.1.3 0 .7-.2 1z"/></svg>
    </div>
    <div class="contact__text">+03 9172 5843</div>
  </div>

  <div class="contact contact--mail">
    <div class="contact__icon">
      <svg width="26" height="18" viewBox="0 0 26 18"><rect x="1" y="1" width="24" height="16" fill="#fff" stroke="#fff"/><path d="M1 1l12 9 12-9" fill="none" stroke="#44494f" stroke-width="1.6"/></svg>
    </div>
    <div class="contact__text">kvtmarts@mailnest.example</div>
  </div>

  <div class="contact contact--place">
    <div class="contact__icon">
      <svg width="24" height="28" viewBox="0 0 24 28"><path d="M12 2a7 7 0 0 0-7 7c0 5 7 12 7 12s7-7 7-12a7 7 0 0 0-7-7z" fill="#fff"/><circle cx="12" cy="9" r="2.6" fill="#5f6b73"/><ellipse cx="12" cy="24" rx="10" ry="3" fill="none" stroke="#fff" stroke-width="1.4"/></svg>
    </div>
    <div class="contact__text">Thomastown<br>482 Elm Parade</div>
  </div>
</section>

<section class="card card--back">
  <div class="back-band back-band--top"></div>
  <div class="back-brand">
    <div class="back-brand__name">KVT Groceries &amp; Spices</div>
    <div class="back-brand__tagline">Trusted Name Since 2008</div>
  </div>
  <div class="back-band back-band--bottom">
    <svg width="28" height="19" viewBox="0 0 26 18"><rect x="1" y="1" width="24" height="16" fill="#fff" stroke="#fff"/><path d="M1 1l12 9 12-9" fill="none" stroke="#e31e25" stroke-width="1.6"/></svg>
    <span>kvtmarts@mailnest.example</span>
  </div>
</section>

</body>
</html>
```